Real Estate Business card design

Company Name: Tamarind Holdings, LLC
subtitle: We pay cash for houses!
Daniel Whitcombe
Managing Director
555-214-0963
Dan@TamarindHoldingsLLC.example
www.TamarindHoldingsLLC.example

We pay referral fees for Seller and Buyer leads.

Back:
We offer referral fees for Seller and Buyer leads that close.

Please contact Hal at 555-214-0963 with your referrals or to learn more about the referral program!

I am open to different color options but I am going for a classic, elegant, clean, and professional look. Please use logo as a reference.

Target Market(s)

People selling their homes and people in the market for buying homes.

Contact Information for Business Card

please see project description

Font styles to use
Serif
Sans Serif
Script

Requirements
Must have
• must have my logo in it
Nice to have
• I like cards that are split down the middle but please come up with a few mock ups. Open to any color scheme.

```html
<!DOCTYPE html>
<html lang="en">
<head>
<meta charset="utf-8">
<title>Tamarind Holdings, LLC — Business Card</title>
<link href="https://fonts.googleapis.com/css2?family=Open+Sans:ital,wght@0,400;0,600;1,400&display=swap" rel="stylesheet">
<style>
  :root {
    --bg: #ececec;
    --card: #ffffff;
    --ink: #333c4b;
    --gold: #b08758;
    --gold-soft: #c9a275;
    --rule: #d4b48c;
  }
  * { margin: 0; padding: 0; box-sizing: border-box; }
  html, body { width: 1200px; height: 1200px; overflow: hidden; }
  body {
    background: var(--bg);
    font-family: "Open Sans", Arial, sans-serif;
    color: var(--ink);
    display: flex;
    flex-direction: column;
    align-items: center;
    justify-content: center;
    gap: 70px;
  }
  .card {
    width: 840px;
    height: 480px;
    background: var(--card);
    box-shadow: 0 6px 22px rgba(0,0,0,0.10);
    position: relative;
  }

  /* Brand name block */
  .brand { display: flex; align-items: center; gap: 14px; }
  .brand-mark { width: 16px; height: 16px; background: var(--gold-soft); flex: none; }
  .brand-name {
    font-weight: 600;
    color: var(--ink);
    line-height: 1.1;
  }
  .brand-tagline {
    font-style: italic;
    color: var(--ink);
    font-size: 19px;
    margin-top: 10px;
  }

  /* Front */
  .card-front { display: flex; align-items: center; padding: 0 60px; }
  .front-brand { width: 340px; }
  .front-brand .brand-name { font-size: 34px; }
  .divider { width: 1.5px; height: 230px; background: var(--rule); margin: 0 40px 0 20px; }
  .front-details { flex: 1; }
  .person-name {
    font-size: 32px;
    letter-spacing: 1px;
    color: var(--gold);
    text-transform: uppercase;
    font-weight: 400;
  }
  .person-role {
    font-size: 15px;
    color: var(--ink);
    margin-top: 4px;
    letter-spacing: 0.5px;
  }
  .referral-note {
    font-style: italic;
    color: var(--gold);
    font-size: 19px;
    line-height: 1.35;
    margin: 16px 0 20px;
  }
  .contact-list { list-style: none; font-size: 17px; line-height: 1.6; }
  .contact-list li { display: flex; }
  .contact-label { color: var(--gold); width: 32px; flex: none; }

  /* Back */
  .card-back {
    display: flex; flex-direction: column; align-items: center; justify-content: center;
    text-align: center;
  }
  .card-back .brand-name { font-size: 40px; }
  .back-lead, .back-contact {
    font-style: italic; color: var(--gold); font-size: 20px; line-height: 1.4;
  }
  .back-lead { margin-top: 30px; }
  .star { width: 18px; height: 18px; margin: 18px 0; fill: #7d5a36; }
</style>
</head>
<body>

  <section class="card card-front" aria-label="Card front">
    <div class="front-brand">
      <div class="brand">
        <span class="brand-mark"></span>
        <span class="brand-name">Tamarind Holdings, LLC</span>
      </div>
      <p class="brand-tagline">we pay cash for houses!</p>
    </div>
    <div class="divider"></div>
    <div class="front-details">
      <h1 class="person-name">Daniel Whitcombe</h1>
      <p class="person-role">Managing Director</p>
      <p class="referral-note">We pay referral fees for<br>Seller and Buyer leads.</p>
      <ul class="contact-list">
        <li><span class="contact-label">T :</span>555-214-0963</li>
        <li><span class="contact-label">W :</span>www.TamarindHoldingsLLC.example</li>
        <li><span class="contact-label">E :</span>dan@tamarindholdingsllc.example</li>
      </ul>
    </div>
  </section>

  <section class="card card-back" aria-label="Card back">
    <div class="brand">
      <span class="brand-mark"></span>
      <span class="brand-name">Tamarind Holdings, LLC</span>
    </div>
    <p class="back-lead">We offer referral fees for<br>Seller and Buyer leads that close.</p>
    <svg class="star" viewBox="0 0 24 24" aria-hidden="true">
      <polygon points="12,1 15,9 23,9 16.5,14 19,22 12,17 5,22 7.5,14 1,9 9,9"/>
    </svg>
    <p class="back-contact">Please contact Hal at 555-214-0963<br>with your referrals or to learn more about the referral program!</p>
  </section>

</body>
</html>
```